Hi, We are global cloud printer looking to start a ad print run, we require full and half page print ad's designed with the following dimensions

Full page dimensions:

Image area: 345 mm in height x 260 mm (6 columns) in width
Trim area: 368 mm in height x 280 mm (6 columns) in width
Bleed area: 371 mm in height x 283 mm (6 columns) in width

Half-page dimensions:
270 mm in height x 172 mm (4 columns) in width

We want a minimalistic ad that really stands out from the crowd, with a full page we want it to make an impact and drive people towards our site.

The site is www.plaventro.com , we would like to match the look and feel but would like the wow factor so our open to all concepts.

We would like the following tagline incorporated in the Ad The cloud you've been waiting for, might be closer than you think.

```html
<!DOCTYPE html>
<html lang="en">
<head>
<meta charset="utf-8">
<title>Plaventro – The cloud you've been waiting for</title>
<link rel="stylesheet" href="https://fonts.googleapis.com/css2?family=Open+Sans:wght@600;700&family=Roboto:ital,wght@0,300;1,300&family=Roboto+Condensed:ital,wght@1,800&display=swap">
<style>
  :root {
    --sky-top: #3873c2;
    --sky-mid: #7eaadb;
    --sky-low: #a9c4e3;
    --sky-base: #e4ebf4;
    --cloud-white: rgba(255, 255, 255, 0.92);
    --cloud-haze: rgba(236, 242, 250, 0.55);
    --accent-green: #9ccb3b;
    --ink: #111418;
    --tagline-white: #ffffff;
  }
  * { margin: 0; padding: 0; box-sizing: border-box; }
  html, body { width: 913px; height: 1200px; overflow: hidden; }
  body { background: var(--sky-base); }

  .ad {
    position: relative;
    width: 913px;
    height: 1200px;
    overflow: hidden;
    background: linear-gradient(180deg,
      var(--sky-top) 0%,
      #4c86cc 30%,
      var(--sky-mid) 58%,
      var(--sky-low) 82%,
      var(--sky-base) 100%);
  }

  .brand-name {
    position: absolute;
    left: 48px;
    top: 28px;
    font-family: "Open Sans", sans-serif;
    font-weight: 600;
    font-size: 62px;
    letter-spacing: -1.5px;
    color: var(--ink);
    line-height: 1;
  }

  .cloud-visual {
    position: absolute;
    left: 190px;
    top: 100px;
    width: 700px;
    height: 340px;
    background: radial-gradient(closest-side at 50% 50%,
      var(--cloud-white) 0%,
      var(--cloud-haze) 55%,
      rgba(255, 255, 255, 0) 100%);
  }

  .tagline {
    position: absolute;
    inset: 0;
    pointer-events: none;
    font-weight: normal;
  }
  .tagline span { position: absolute; white-space: nowrap; line-height: 1; }

  .tagline .light {
    font-family: "Roboto", sans-serif;
    font-weight: 300;
    font-style: italic;
    color: var(--tagline-white);
  }
  .tagline .keyword {
    font-family: "Roboto Condensed", sans-serif;
    font-weight: 800;
    font-style: italic;
    color: var(--accent-green);
    letter-spacing: -1px;
    transform-origin: left;
  }

  .word-the      { left: 46px;  top: 522px; font-size: 72px; letter-spacing: -2px; }
  .word-cloud    { left: 176px; top: 444px; font-size: 162px; transform: scaleX(1.1); }
  .word-waiting1 { left: 568px; top: 476px; font-size: 54px; letter-spacing: 1px; word-spacing: 10px; }
  .word-waiting2 { left: 553px; top: 544px; font-size: 54px; letter-spacing: 1.5px; word-spacing: 8px; }
  .word-closer   { left: 75px;  top: 612px; font-size: 52px; word-spacing: 10px; }
  .word-think    { left: 678px; top: 594px; font-size: 94px; transform: scaleX(1.0); }

  .site-address {
    position: absolute;
    right: 22px;
    bottom: 14px;
    font-family: "Open Sans", sans-serif;
    font-weight: 700;
    font-size: 42px;
    letter-spacing: -0.5px;
    color: var(--ink);
    line-height: 1;
  }
</style>
</head>
<body>
  <main class="ad">
    <div class="brand-name">plaventro</div>

    <div class="cloud-visual" role="img" aria-label="Photograph of a single white fluffy cloud in a blue sky"></div>

    <h1 class="tagline" aria-label="The cloud you've been waiting for, might be closer than you think.">
      <span class="light word-the">The</span>
      <span class="keyword word-cloud">cloud</span>
      <span class="light word-waiting1">you’ve been</span>
      <span class="light word-waiting2">waiting for,</span>
      <span class="light word-closer">might be closer than you</span>
      <span class="keyword word-think">think.</span>
    </h1>

    <div class="site-address">www.plaventro.com</div>
  </main>
</body>
</html>
```